Employee I.D. Card - Badge

We need an employee I.D. card designed. Our employees are going to be wearing these. I would like to have it look nice. Something professional yet cool (not uptight if that makes sense).
Project Scope:
Vertical orientation
Company name ------------- (Bright and Tidy)
Website ------------- (brightandtidymn.example)
Employee Picture
background check image
front and back designed - same design on either side
You can create the card without having the employee images on them.
Here are the dimensions -
2.125 x 3.370 inches
Double sided - same design can be used front and back
Background badge - I would like to add an image that shows that the employee has taken a background check. I've added the press-kit for the company we use. If you have a better idea than incorporating their logo, we can certainly do something different.
Example image-
https://www.findwell-search.example/results?q=background+check+badge&mode=images
The print company will set up the names.
Logo is attached
Also attached are our business cards. You can use this for an idea of brand/company style.
Our website - brightandtidymn.example

```html
<!DOCTYPE html>
<html lang="en">
<head>
<meta charset="utf-8">
<title>Bright and Tidy – Employee ID Badges</title>
<link rel="stylesheet" href="https://fonts.googleapis.com/css2?family=Lato:wght@400;700&display=swap">
<style>
  :root {
    --page-bg: #e9eaec;
    --card-navy: #062f57;
    --brand-blue: #1398d8;
    --band-blue: #0a93d6;
    --band-blue-deep: #0781c8;
    --band-green: #afd33a;
    --band-green-deep: #98c630;
    --photo-bg: #e6e6e6;
    --photo-figure: #9a9a9a;
    --seal-dark: #2f3335;
    --seal-ring: #0d2a4a;
    --text-light: #ffffff;
  }
  * { margin: 0; padding: 0; box-sizing: border-box; }
  html, body {
    width: 1200px;
    height: 1200px;
    overflow: hidden;
    background: var(--page-bg);
  }
  .canvas {
    position: relative;
    width: 1200px;
    height: 1200px;
  }
  .badge-card {
    position: absolute;
    top: 310px;
    width: 364px;
    height: 594px;
    background: var(--card-navy);
    overflow: hidden;
    box-shadow: 0 2px 6px rgba(0,0,0,0.25);
  }
  .badge-card--blue { left: 234px; }
  .badge-card--green { left: 630px; }

  .brand-name {
    position: absolute;
    top: 78px;
    left: 0;
    width: 100%;
    text-align: center;
    font-family: "Lato", sans-serif;
    font-weight: 700;
    font-size: 38px;
    line-height: 1;
    color: var(--brand-blue);
    letter-spacing: -0.5px;
  }
  .brand-url {
    position: absolute;
    top: 187px;
    left: 0;
    width: 100%;
    text-align: center;
    font-family: "Lato", sans-serif;
    font-weight: 400;
    font-size: 16px;
    color: var(--text-light);
  }
  .employee-photo {
    position: absolute;
    left: 88px;
    width: 189px;
    height: 190px;
    background: linear-gradient(180deg, var(--photo-bg) 0%, #dcdcdc 100%);
  }
  .badge-card--blue .employee-photo { top: 241px; }
  .badge-card--green .employee-photo { top: 224px; }

  .color-band {
    position: absolute;
    left: 0;
    bottom: 0;
    width: 100%;
    height: 78px;
  }
  .badge-card--blue .color-band {
    background: linear-gradient(180deg, var(--band-blue) 0%, var(--band-blue-deep) 100%);
  }
  .badge-card--green .color-band {
    background: linear-gradient(180deg, var(--band-green) 0%, var(--band-green-deep) 100%);
  }
  .clearance-seal {
    position: absolute;
    left: 112px;
    top: 436px;
    width: 140px;
    height: 140px;
  }
</style>
</head>
<body>
<main class="canvas">

  <section class="badge-card badge-card--blue">
    <div class="brand-name">Bright and Tidy</div>
    <div class="brand-url">brightandtidymn.example</div>
    <div class="employee-photo" role="img" aria-label="Employee portrait photo placeholder"></div>
    <div class="color-band"></div>
    <svg class="clearance-seal" viewBox="0 0 140 140" role="img" aria-label="Background check cleared seal">
      <circle cx="70" cy="70" r="69" fill="var(--seal-ring)"/>
      <circle cx="70" cy="70" r="60" fill="var(--seal-dark)"/>
      <circle cx="70" cy="70" r="30" fill="none" stroke="#6b7073" stroke-width="2"/>
    </svg>
  </section>

  <section class="badge-card badge-card--green">
    <div class="brand-name">Bright and Tidy</div>
    <div class="brand-url">brightandtidymn.example</div>
    <div class="employee-photo" role="img" aria-label="Employee portrait photo placeholder"></div>
    <div class="color-band"></div>
    <svg class="clearance-seal" viewBox="0 0 140 140" role="img" aria-label="Background check cleared seal">
      <circle cx="70" cy="70" r="69" fill="var(--seal-ring)"/>
      <circle cx="70" cy="70" r="60" fill="var(--seal-dark)"/>
      <circle cx="70" cy="70" r="30" fill="none" stroke="#6b7073" stroke-width="2"/>
    </svg>
  </section>

</main>
</body>
</html>
```